Dr Peter Vandell
Urologist
Professional
Dr Peter Vandell MB,ChB(UCT), FC Urol.(SA)
Ridgeway Medicentre and Lanford Private Hospital PO Box 58147 Brookvale 4105
povandell@medinet-mail.co.za
Pr No 7315824
Please email me for scanned copies of the existing stationery and cards to see current format

```html
<!DOCTYPE html>
<html lang="en">
<head>
<meta charset="utf-8">
<title>Dr Peter Vandell – Stationery</title>
<link rel="stylesheet" href="https://fonts.googleapis.com/css2?family=EB+Garamond:wght@400;500;700&display=swap">
<style>
  :root {
    --backdrop: #ebe6de;
    --paper: #ffffff;
    --brand-red: #a51d22;
    --flap-red: #9e1b20;
    --ink: #3a3a3a;
    --ink-soft: #6b6b6b;
    --fold: #d9d9d9;
    --shadow: rgba(0,0,0,0.18);
  }
  html, body { margin: 0; padding: 0; overflow: hidden; }
  body { width: 1200px; height: 678px; background: var(--backdrop); position: relative; font-family: "EB Garamond", Georgia, serif; color: var(--ink); }
  .sheet { position: absolute; background: var(--paper); box-shadow: 0 2px 6px var(--shadow); }
  .identity { position: absolute; text-align: center; }
  .identity .name { color: var(--brand-red); font-weight: 500; line-height: 1; white-space: nowrap; }
  .identity .degrees { color: var(--ink-soft); letter-spacing: 0.04em; white-space: nowrap; }
  .identity .specialty { color: var(--brand-red); font-weight: 700; }
  .details { position: absolute; line-height: 1.3; color: var(--ink-soft); }
  .details .hospitals { color: var(--ink); font-weight: 700; margin-bottom: 0.6em; }
  .details p { margin: 0; white-space: nowrap; }

  /* Business card */
  .business-card { left: 48px; top: 377px; width: 192px; height: 127px; }
  .business-card .identity { left: 10px; top: 34px; width: 92px; }
  .business-card .name { font-size: 13px; }
  .business-card .degrees { font-size: 4px; margin-top: 2px; }
  .business-card .specialty { font-size: 13px; margin-top: 8px; }
  .business-card .details { left: 108px; top: 28px; font-size: 4.6px; }

  /* Letterhead */
  .letterhead { left: 259px; top: 36px; width: 420px; height: 593px; }
  .letterhead .identity { left: 14px; top: 20px; width: 112px; }
  .letterhead .name { font-size: 16px; }
  .letterhead .degrees { font-size: 5px; margin-top: 2px; }
  .letterhead .specialty { font-size: 16px; margin-top: 10px; }
  .letterhead .details { left: 139px; top: 16px; font-size: 5.4px; }

  /* Envelope front */
  .envelope-front { left: 696px; top: 91px; width: 432px; height: 216px; }
  .envelope-front .identity { left: 10px; top: 20px; width: 122px; }
  .envelope-front .name { font-size: 17px; }
  .envelope-front .degrees { font-size: 5.2px; margin-top: 2px; }
  .envelope-front .specialty { font-size: 17px; margin-top: 10px; }
  .envelope-front .details { left: 140px; top: 16px; font-size: 5.6px; }

  /* Envelope back */
  .envelope-back { left: 696px; top: 336px; width: 432px; height: 293px; background: transparent; box-shadow: none; }
  .envelope-back svg { display: block; }
  .emergency-label { font-family: "EB Garamond", Georgia, serif; font-size: 9px; text-anchor: middle; }
</style>
</head>
<body>

<section class="sheet business-card">
  <div class="identity">
    <div class="name">Dr Peter Vandell</div>
    <div class="degrees">MB,ChB(UCT), FC Urol.(SA)</div>
    <div class="specialty">Urologist</div>
  </div>
  <div class="details">
    <p class="hospitals">Ridgeway Medicentre<br>and Lanford Private Hospital</p>
    <p>Rooms: 033 418 2270</p>
    <p>Fax: 033 418 2271</p>
    <p>Email: povandell@medinet-mail.co.za</p>
    <p>Emergencies: 083 214 6092</p>
  </div>
</section>

<section class="sheet letterhead">
  <div class="identity">
    <div class="name">Dr Peter Vandell</div>
    <div class="degrees">MB,ChB(UCT), FC Urol.(SA)</div>
    <div class="specialty">Urologist</div>
  </div>
  <div class="details">
    <p class="hospitals">Ridgeway Medicentre<br>and Lanford Private Hospital</p>
    <p>PO Box 58147</p>
    <p>Brookvale 4105</p>
    <p>Rooms: 033 418 2270</p>
    <p>Fax: 033 418 2271</p>
    <p>Email: povandell@medinet-mail.co.za</p>
    <p>Emergencies: 083 214 6092</p>
    <p>Pr No 7315824</p>
  </div>
</section>

<section class="sheet envelope-front">
  <div class="identity">
    <div class="name">Dr Peter Vandell</div>
    <div class="degrees">MB,ChB(UCT), FC Urol.(SA)</div>
    <div class="specialty">Urologist</div>
  </div>
  <div class="details">
    <p class="hospitals">Ridgeway Medicentre<br>and Lanford Private Hospital</p>
    <p>PO Box 58147</p>
    <p>Brookvale 4105</p>
    <p>Rooms: 033 418 2270</p>
    <p>Fax: 033 418 2271</p>
    <p>Email: povandell@medinet-mail.co.za</p>
    <p>Pr No 7315824</p>
  </div>
</section>

<section class="sheet envelope-back">
  <svg width="432" height="293" viewBox="0 0 432 293" aria-label="Envelope back with red flap">
    <defs>
      <filter id="soft-shadow" x="-5%" y="-5%" width="110%" height="115%">
        <feDropShadow dx="0" dy="2" stdDeviation="2.5" flood-color="#000" flood-opacity="0.18"/>
      </filter>
    </defs>
    <rect class="envelope-body" x="0" y="20" width="432" height="273" fill="var(--paper)" filter="url(#soft-shadow)"/>
    <path class="side-flaps" d="M0 22 L200 190 M432 22 L232 190" stroke="var(--fold)" stroke-width="1" fill="none"/>
    <path class="bottom-flap" d="M0 293 L216 150 L432 293" fill="#fbfbfb" stroke="var(--fold)" stroke-width="1"/>
    <path class="top-flap" d="M0 0 L432 0 L432 22 Q216 150 216 150 Q216 150 0 22 Z" fill="var(--flap-red)" filter="url(#soft-shadow)"/>
    <text class="emergency-label" x="216" y="52" fill="#f3d9d9">Emergencies:</text>
    <text class="emergency-label" x="216" y="63" fill="#f3d9d9">083 214 6092</text>
    <text class="emergency-label" x="216" y="178" fill="var(--brand-red)">Emergencies:</text>
    <text class="emergency-label" x="216" y="189" fill="var(--brand-red)">083 214 6092</text>
  </svg>
</section>

</body>
</html>
```